Dorian "Keep Our Drums Going"

Hello, looking for a flyer design for our band project, we are an Corbin Tribute artist seeking school band programs to work together on a fundraiser where the school band will join our band for 1 night and be part of the show. Red and Black should be the most dominant colors in the flyer. There is a flyer being used by friends of ours for a similar project it can be found at http://www.copperhalltributes.com/wbns.html

the text for the flyer is as follows, again very similar to what the Marigolds guys are using

Dorian Wells - Corbin Tribute Artist presents

"Keep Our Drums Going"

Bring Corbin Tribute Artist - Dorian Wells from Lanternglow Theatre in Pigeon Forge, TN to your school to perform with your bands, orchestras, and choirs

Dorian has launched a new fundraising program for schools to keep music programs alive in our schools

What you need to know anout this project

* There is absolutely no cost to the school
* Charts to the Corbin songs will be provided
* Your students perform with Dorian Wells & his band during a special section of the show
* Dorian is available for all local media interviews, and assistance in the promotion of the event on behalf of your program
*A portion of the proceeds are shared with the music program

The concert is educational and entertaining, spanning from the early "bubble gum" years through the Vegas era

Great exposure for your school music program to a whole new audience

Wonderful experience for students that is exciting and FUN!!

_________________

I would prefer this design to be on 8.5 x 11 (if longer page is needed, or front and back is ok also)

please find graphics attached , please feel free to use as few or as many as you would like.

Thanks

```html
<!DOCTYPE html>
<html lang="en">
<head>
<meta charset="utf-8">
<title>Dorian Wells – Keep Our Drums Going Flyer</title>
<link rel="stylesheet" href="https://fonts.googleapis.com/css2?family=Alfa+Slab+One&family=Oswald:wght@300;400&family=Open+Sans:wght@400;700&display=swap">
<style>
  :root {
    --stage: #ffffff;
    --paper: #ffffff;
    --ink: #1d1d1d;
    --ink-soft: #2b2b2b;
    --red: #e0401f;
    --white: #ffffff;
    --grey-text: #d6d6d6;
    --shadow: rgba(0,0,0,0.35);
  }
  * { margin: 0; padding: 0; box-sizing: border-box; }
  html, body { width: 1200px; height: 752px; overflow: hidden; background: var(--stage); }
  .canvas { position: relative; width: 1200px; height: 752px; }

  .flyer {
    position: absolute; top: 20px; width: 546px; height: 702px;
    background: var(--paper); padding: 12px;
    box-shadow: 0 2px 8px var(--shadow);
  }
  .flyer--front { left: 43px; }
  .flyer--back { left: 619px; }
  .flyer__sheet {
    position: relative; width: 100%; height: 100%; overflow: hidden;
    background: radial-gradient(ellipse at 45% 45%, var(--ink-soft) 0%, var(--ink) 70%);
  }
  .abs { position: absolute; }

  .ornament {
    background: radial-gradient(ellipse at center, rgba(255,255,255,0.08) 0%, rgba(255,255,255,0) 70%);
  }
  .performer-figure { background: var(--red); border-radius: 40px 40px 6px 6px; }
  .performer-photo {
    background: linear-gradient(160deg, #3a2a24 0%, #8a6a58 40%, #e8e4de 75%, #f6f4f0 100%);
  }
  .stage-photo {
    background: linear-gradient(180deg, #111 0%, #3b2e28 45%, #e9e6e0 70%, #c9362a 100%);
  }

  .name-first, .name-last {
    font-family: "Alfa Slab One", serif; color: var(--white); line-height: 1; white-space: nowrap;
  }
  .name-first { transform: scaleY(1.6); transform-origin: left top; }
  .tagline, .presents {
    font-family: "Oswald", sans-serif; font-weight: 400; color: var(--white);
    line-height: 1; text-transform: uppercase; white-space: nowrap;
  }
  .presents { letter-spacing: 9px; }
  .campaign {
    font-family: "Alfa Slab One", serif; color: var(--red); line-height: 1; white-space: nowrap;
  }
  .pitch {
    font-family: "Open Sans", sans-serif; font-weight: 700; color: var(--white);
    font-size: 13px; line-height: 1.2;
  }
  .pitch p + p { margin-top: 12px; }
  .web {
    font-family: "Open Sans", sans-serif; font-weight: 700; color: var(--red); font-size: 14px;
    white-space: nowrap;
  }

  .section-title {
    font-family: "Alfa Slab One", serif; color: var(--red); font-size: 24px; line-height: 1; white-space: nowrap;
  }
  .section-sub {
    font-family: "Oswald", sans-serif; font-weight: 400; color: var(--white);
    font-size: 13px; letter-spacing: 1px; text-transform: uppercase; white-space: nowrap;
  }
  .copy {
    font-family: "Open Sans", sans-serif; color: var(--grey-text); font-size: 10.5px; line-height: 1.55;
  }
  .copy p { margin-bottom: 12px; }
  .benefits { list-style: none; margin-bottom: 12px; }
  .benefits li {
    font-weight: 700; color: var(--white); padding-left: 8px; text-indent: -8px; margin-bottom: 1px;
  }
  .benefits li::before { content: "- "; }
</style>
</head>
<body>
<div class="canvas">

  <!-- Front page -->
  <section class="flyer flyer--front">
    <div class="flyer__sheet">
      <div class="abs ornament" style="left:380px; top:0; width:142px; height:405px;" role="img" aria-label="Faint decorative treble clef and swirling music notes"></div>
      <div class="abs performer-figure" style="left:118px; top:0; width:113px; height:253px;" role="img" aria-label="Red silhouette of the performer in a jumpsuit singing into a microphone"></div>

      <div class="abs name-first" style="left:26px; top:56px; font-size:67px;">DORIAN</div>
      <div class="abs name-last" style="left:26px; top:186px; font-size:74px;">WELLS</div>
      <div class="abs tagline" style="left:27px; top:264px; font-size:33px;">Corbin Tribute Artist</div>
      <div class="abs presents" style="left:28px; top:296px; font-size:56px;">Presents</div>
      <div class="abs campaign" style="left:29px; top:352px; font-size:28px;">KEEP OUR DRUMS</div>
      <div class="abs campaign" style="left:28px; top:380px; font-size:60px;">GOING</div>

      <div class="abs performer-photo" style="left:306px; top:400px; width:216px; height:278px;" role="img" aria-label="Photo of the tribute artist in a white studded jumpsuit singing passionately into a microphone"></div>

      <div class="abs pitch" style="left:28px; top:470px; width:255px;">
        <p>Bring Corbin Tribute Artist - Dorian Wells from Lanternglow Theatre in Pigeon Forge, TN to your school to perform with your bands, orchestras, and choirs.</p>
        <p>Dorian has launched a new fundraising program for schools to keep music programs alive in our schools.</p>
      </div>
      <div class="abs web" style="left:28px; top:640px;">www.dorianwellstribute.com</div>
    </div>
  </section>

  <!-- Back page -->
  <section class="flyer flyer--back">
    <div class="flyer__sheet">
      <div class="abs ornament" style="left:360px; top:40px; width:162px; height:355px;" role="img" aria-label="Faint decorative treble clef and swirling music notes"></div>

      <div class="abs section-title" style="left:24px; top:24px;">INVOLVE YOUR SCHOOL</div>
      <div class="abs section-sub" style="left:24px; top:50px;">Wonderfully engaging &amp; exciting for students</div>

      <div class="abs copy" style="left:24px; top:84px; width:335px;">
        <p>Join with Dorian Wells' revolutionary fundraising program and your school's music program will benefit from additional funding with a proportion of the proceeds being donated to your school.</p>
        <ul class="benefits">
          <li>Absolutely no cost to your school</li>
          <li>Charts to the Corbin songs will be provided</li>
          <li>Your students perform with Dorian &amp; his band during a special section of the performance.</li>
          <li>Dorian is available for all local media interviews, and assistance in the promotion of the event on behalf of your program.</li>
          <li>A portion of the proceeds are shared with your music program.</li>
        </ul>
        <p>The concert is educational and entertaining, spanning from the early "bubble gum" years through the Vegas era.</p>
        <p>Great exposure for your school music program to a whole new audience.</p>
      </div>

      <div class="abs performer-figure" style="left:90px; top:420px; width:93px; height:173px;" role="img" aria-label="Red silhouette of the performer in a jumpsuit singing into a microphone"></div>
      <div class="abs name-first" style="left:24px; top:432px; font-size:58px;">DORIAN</div>
      <div class="abs name-last" style="left:26px; top:532px; font-size:58px;">WELLS</div>
      <div class="abs tagline" style="left:27px; top:604px; font-size:25px;">Corbin Tribute Artist</div>
      <div class="abs web" style="left:27px; top:640px;">www.dorianwellstribute.com</div>

      <div class="abs stage-photo" style="left:302px; top:408px; width:220px; height:270px;" role="img" aria-label="Stage photo of the tribute artist in a white jumpsuit with red scarf singing in front of an orchestra"></div>
    </div>
  </section>

</div>
</body>
</html>
```